Header for Academic Handouts (How-to-Guides)

We are looking for a design element, which can be used as a visual header on A4-word-documents (Portrait-Set-Up). It shall be a graphic, visual language which is clearly understandable. The header height shall be between 0.75 - 1.5 inch – so it should not have too many small details. Attached below ideas/directions how the final document could look like.

The visual element shall symbolize by simple means the topic of “flipped classroom” or “active learning”. The documents with these new graphic elements will be used on handouts which are distributed in this training course:
https://www.korvanel.ch/en/the-korvanel-academy/education/educational-development/didaktische-weiterbildung/flipped-classroom.html

```html
<!DOCTYPE html>
<html lang="en">
<head>
<meta charset="utf-8">
<title>Korvanel – Flipped Classroom Guide</title>
<link rel="stylesheet" href="https://fonts.googleapis.com/css2?family=Arimo:wght@400;700&display=swap">
<style>
  :root {
    --canvas-bg: #f5f1ef;
    --paper: #ffffff;
    --navy: #1f3f7a;
    --navy-deep: #1a3d78;
    --mist: #e9e9f1;
    --mark-dot: #1f3f7a;
  }
  * { margin: 0; padding: 0; box-sizing: border-box; }
  html, body {
    width: 1200px;
    height: 1200px;
    overflow: hidden;
    background: var(--canvas-bg);
    font-family: "Arimo", Arial, sans-serif;
  }
  .page {
    position: absolute;
    left: 253px;
    top: 96px;
    width: 737px;
    height: 1032px;
    background: var(--paper);
    box-shadow: 1px 2px 3px rgba(0,0,0,0.12);
  }
  .header-band {
    position: absolute;
    left: 0;
    top: 0;
    width: 100%;
    height: 103px;
    background: linear-gradient(90deg,
      var(--paper) 0%,
      var(--paper) 37%,
      var(--mist) 48%,
      #a4a6c3 66%,
      #5b6892 86%,
      var(--navy-deep) 100%);
  }
  .header-rule {
    position: absolute;
    left: 0;
    top: 109px;
    width: 100%;
    height: 2px;
    background: linear-gradient(90deg, var(--navy) 0%, var(--navy) 45%, rgba(31,63,122,0.15) 100%);
  }
  .brand-dot {
    position: absolute;
    left: 73px;
    top: 48px;
    width: 44px;
    height: 44px;
    border-radius: 50%;
    background: var(--mark-dot);
  }
  .brand-name {
    position: absolute;
    left: 141px;
    top: 46px;
    font-size: 29px;
    font-weight: 700;
    color: var(--navy);
    line-height: 1;
  }
  .guide-title {
    position: absolute;
    left: 141px;
    top: 78px;
    font-size: 14px;
    font-weight: 400;
    color: var(--navy);
    line-height: 1;
  }
  .footer-rule {
    position: absolute;
    left: 0;
    top: 991px;
    width: 100%;
    height: 1px;
    background: linear-gradient(90deg, rgba(31,63,122,0) 0%, rgba(31,63,122,0.45) 30%, var(--navy) 100%);
  }
  .footer-url {
    position: absolute;
    left: 0;
    top: 1002px;
    width: 100%;
    text-align: center;
    font-size: 10px;
    color: var(--navy);
  }
</style>
</head>
<body>
  <main class="page">
    <header>
      <div class="header-band"></div>
      <div class="header-rule"></div>
      <span class="brand-dot"></span>
      <div class="brand-name">Korvanel</div>
      <div class="guide-title">Flipped Classroom Guide</div>
    </header>
    <footer>
      <div class="footer-rule"></div>
      <div class="footer-url">www.korvanel.ch</div>
    </footer>
  </main>
</body>
</html>
```